6 - 8 'Holistic' Instagram Graphics

Hi there!
We are looking to build up a library of Graphic Templates to use as Instagram & Facebook posts for our Holistic Medi Spa (& 3 other companies eventually)
This competition is for a sample of 6 - 8 designs. For the winner(s), we will make an agreement for a batch order (Looking for 200+ designs in total), and will be looking to make a long term arrangement.
Please find a full job description in the attached Word Document.
Any questions, don't hesitate to ask.
Thanks!
Medical Spa

```html
<!DOCTYPE html>
<html lang="en">
<head>
<meta charset="utf-8">
<title>Beauty &amp; Spa Center – Instagram Post Set</title>
<link rel="stylesheet" href="https://fonts.googleapis.com/css2?family=Allura&family=Cormorant+Garamond:wght@500&family=Montserrat:wght@400;600;800&family=Yellowtail&display=swap">
<style>
:root{
  --blue:#0b8ed6;
  --blue-deep:#0a7fc4;
  --blue-soft:#6cc4ea;
  --mist:#e7f4fb;
  --mist-mid:#c8e7f7;
  --teal:#12a27c;
  --ink:#1b1b1b;
  --white:#ffffff;
  --script:'Yellowtail','Allura',cursive;
  --fine-script:'Allura',cursive;
  --sans:'Montserrat',sans-serif;
  --serif:'Cormorant Garamond',serif;
}
*{box-sizing:border-box;margin:0;padding:0}
html,body{width:800px;height:1200px;overflow:hidden;background:var(--white)}
.canvas{position:relative;width:800px;height:1200px;background:var(--white);font-family:var(--sans)}
.post{position:absolute;width:305px;height:305px;overflow:hidden;background:var(--mist)}
.post svg.shapes{position:absolute;inset:0;width:305px;height:305px}
.abs{position:absolute}
.photo{position:absolute}
.script{font-family:var(--script);line-height:1;white-space:nowrap}
.white{color:var(--white)}
.blue{color:var(--blue)}
.small-label{font-size:8.5px;font-weight:600;letter-spacing:.3px;white-space:nowrap}
.phone-line{font-size:9px;letter-spacing:1.6px;white-space:nowrap}
.badge{position:absolute;border-radius:50%;display:flex;flex-direction:column;align-items:center;justify-content:center;color:var(--white);font-weight:600;font-size:12px;line-height:1.2}

/* post positions */
.post--massage{left:85px;top:122px}
.post--offer{left:410px;top:122px}
.post--review{left:85px;top:447px}
.post--giveaway{left:410px;top:447px}
.post--pedicure{left:85px;top:772px}
.post--natural{left:410px;top:772px;background:#eef7fc}

/* review card */
.review-card{position:absolute;left:50px;top:55px;width:206px;height:220px;background:var(--white);border-radius:10px;padding:26px 16px 0}
.review-avatar{position:absolute;left:131px;top:33px;width:42px;height:42px;border-radius:50%;border:3px solid var(--white);background:linear-gradient(135deg,#c46a7a,#3a2a2e)}
.review-stars{text-align:center;color:var(--blue);font-size:9px;letter-spacing:1px}
.review-name{text-align:center;font-weight:600;font-size:12px;color:var(--ink);margin:5px 0 10px}
.review-text{font-size:10px;line-height:1.45;color:var(--ink)}
.review-text p+p{margin-top:9px}
.review-icons{position:absolute;left:16px;bottom:15px;display:flex;gap:5px}
.review-signature{position:absolute;right:16px;bottom:12px;width:66px;height:20px;background:linear-gradient(90deg,#e9e9e9,#cfcfcf);border-radius:3px}

/* natural treatment heading */
.natural-title{position:absolute;right:12px;top:24px;width:150px;text-align:center;font-family:var(--fine-script);font-size:50px;line-height:1;color:var(--ink);white-space:nowrap}
.natural-sub{position:absolute;right:18px;top:84px;width:140px;text-align:center;font-family:var(--serif);font-size:25px;color:var(--ink);white-space:nowrap}
</style>
</head>
<body>
<main class="canvas">

  <!-- Post 1 -->
  <section class="post post--massage">
    <div class="photo" role="img" aria-label="Photo of a smiling woman receiving a shoulder massage" style="inset:0;background:linear-gradient(135deg,#e9e2da 0%,#d9b9a2 45%,#6b4a36 100%)"></div>
    <svg class="shapes" viewBox="0 0 305 305" aria-hidden="true">
      <path d="M0 90 C30 80 55 100 50 140 C45 175 70 205 110 205 C150 205 170 235 220 240 C260 244 285 225 305 222 L305 305 L0 305 Z" fill="var(--blue)"/>
      <path d="M0 85 C25 80 40 100 32 125 L0 130 Z" fill="var(--blue-soft)"/>
    </svg>
    <div class="abs script white" style="left:25px;top:215px;font-size:29px">Beauty &amp;<br>Spa center</div>
    <div class="abs small-label white" style="left:173px;top:254px">book an appointment</div>
    <div class="abs phone-line white" style="left:173px;top:270px">555-014-2368</div>
  </section>

  <!-- Post 2 -->
  <section class="post post--offer">
    <svg class="shapes" viewBox="0 0 305 305" aria-hidden="true">
      <path d="M0 0 L60 0 C70 25 40 45 15 45 L0 45 Z" fill="var(--mist-mid)"/>
      <path d="M0 160 C30 150 60 175 75 215 C90 250 130 270 175 305 L0 305 Z" fill="var(--blue)"/>
      <path d="M240 285 C260 270 290 275 305 265 L305 305 L225 305 Z" fill="var(--mist-mid)"/>
    </svg>
    <div class="photo" role="img" aria-label="Photo of cream jars, a makeup brush and a pink flower on blue" style="left:137px;top:46px;width:137px;height:212px;background:linear-gradient(160deg,#1a9fe0,#0b86cc)"></div>
    <div class="abs script blue" style="left:24px;top:86px;font-size:24px;line-height:1.1">Beauty &amp;<br>Spa center</div>
    <div class="badge" style="left:24px;top:168px;width:58px;height:54px;background:var(--blue-soft)">25%<span>OFF</span></div>
    <div class="abs small-label white" style="left:24px;top:251px">Book now</div>
    <div class="abs phone-line white" style="left:24px;top:265px">555-014-2368</div>
  </section>

  <!-- Post 3 -->
  <section class="post post--review">
    <svg class="shapes" viewBox="0 0 305 305" aria-hidden="true">
      <path d="M0 0 L110 0 C100 35 60 40 30 30 C15 25 5 30 0 35 Z" fill="var(--mist-mid)"/>
      <path d="M0 120 C20 110 45 130 40 170 L0 180 Z" fill="var(--mist-mid)"/>
      <path d="M210 305 C220 270 260 255 305 250 L305 305 Z" fill="var(--mist-mid)"/>
      <path d="M0 55 C40 40 60 70 95 40 C120 20 100 5 80 10" fill="none" stroke="var(--blue-soft)" stroke-width="1"/>
      <path d="M150 305 C160 270 210 290 250 260 C280 240 300 250 305 235" fill="none" stroke="var(--blue-soft)" stroke-width="1"/>
    </svg>
    <div class="review-card">
      <div class="review-stars">★★★★★</div>
      <div class="review-name">Marla Quenby</div>
      <div class="review-text">
        <p>"For over 10 years, we've been developing new technology for enterprises of all sizes.</p>
        <p>Our mission is to provide companies with cutting-edge products that enable employees to work better and smarter."</p>
      </div>
      <div class="review-icons" aria-hidden="true">
        <svg width="10" height="9" viewBox="0 0 10 9"><path d="M5 9 L1 5 A2.3 2.3 0 0 1 5 1.6 A2.3 2.3 0 0 1 9 5 Z" fill="var(--mist-mid)"/></svg>
        <svg width="10" height="9" viewBox="0 0 10 9"><path d="M0 0 H10 V6 H4 L1 9 V6 H0 Z" fill="var(--mist-mid)"/></svg>
        <svg width="10" height="9" viewBox="0 0 10 9"><circle cx="8" cy="1.5" r="1.5" fill="var(--mist-mid)"/><circle cx="2" cy="4.5" r="1.5" fill="var(--mist-mid)"/><circle cx="8" cy="7.5" r="1.5" fill="var(--mist-mid)"/><path d="M8 1.5 L2 4.5 L8 7.5" stroke="var(--mist-mid)" fill="none"/></svg>
      </div>
      <div class="review-signature" role="img" aria-label="Handwritten signature"></div>
    </div>
    <div class="review-avatar" role="img" aria-label="Portrait photo of the reviewer"></div>
  </section>

  <!-- Post 4 -->
  <section class="post post--giveaway">
    <svg class="shapes" viewBox="0 0 305 305" aria-hidden="true">
      <path d="M0 0 L80 0 C75 25 55 40 30 50 C15 56 5 70 0 80 Z" fill="var(--blue)"/>
      <path d="M0 45 C25 40 45 30 58 0" fill="none" stroke="var(--white)" stroke-width="1"/>
      <path d="M145 305 C165 260 220 250 260 230 C285 218 300 215 305 215 L305 305 Z" fill="var(--mist-mid)"/>
    </svg>
    <div class="abs blue" style="left:0;width:305px;top:86px;text-align:center;font-family:var(--fine-script);font-size:52px;line-height:1">Special</div>
    <div class="abs blue" style="left:0;width:305px;top:150px;text-align:center;font-weight:800;font-size:35px;letter-spacing:.5px">GIVEAWAY!</div>
    <div class="abs blue" style="left:0;width:305px;top:194px;text-align:center;font-size:8.5px">Check out our latest post for details.</div>
    <div class="abs blue" style="left:0;width:305px;top:264px;text-align:center;font-size:10.5px;font-weight:600">www.serenawellspa.com</div>
  </section>

  <!-- Post 5 -->
  <section class="post post--pedicure">
    <div class="photo" role="img" aria-label="Photo of feet soaking in a wooden bowl with floating white flowers" style="inset:0;background:linear-gradient(160deg,#5a4a44 0%,#3a2a24 45%,#6a5a52 100%)"></div>
    <svg class="shapes" viewBox="0 0 305 305" aria-hidden="true">
      <path d="M0 0 H305 V110 C280 120 250 105 220 120 C190 135 160 115 130 100 C100 85 70 95 50 120 C35 140 10 135 0 130 Z" fill="var(--blue)"/>
      <path d="M0 0 H70 C60 15 30 20 0 18 Z" fill="var(--blue-soft)"/>
      <path d="M240 305 C250 285 280 275 305 280 V305 Z" fill="var(--blue-soft)"/>
    </svg>
    <div class="abs script white" style="right:28px;top:32px;font-size:25px">Beauty &amp; Spa center</div>
    <div class="abs small-label white" style="right:30px;top:75px">Book now</div>
    <div class="abs phone-line white" style="right:28px;top:89px">555-014-2368</div>
    <div class="badge" style="left:29px;top:80px;width:56px;height:52px;background:var(--teal)">50%<span>OFF</span></div>
  </section>

  <!-- Post 6 -->
  <section class="post post--natural">
    <div class="photo" role="img" aria-label="Photo of a relaxed woman with a towel wrap beside a yellow lotus flower" style="left:0;top:0;width:165px;height:305px;background:linear-gradient(180deg,#1a8fe0 0%,#7cc3ee 30%,#f1efe9 55%,#e6d3a8 100%)"></div>
    <svg class="shapes" viewBox="0 0 305 305" aria-hidden="true">
      <path d="M166 163 H305 V197 H175 C170 190 178 185 170 178 C176 172 168 168 166 163 Z" fill="var(--blue)"/>
    </svg>
    <div class="natural-title">Natural</div>
    <div class="natural-sub">Treatment</div>
    <div class="abs white" style="right:36px;top:169px;text-align:right;font-size:8px;line-height:1.5;white-space:nowrap">Call for details<br><b style="font-size:9.5px">+555-014-2368</b></div>
    <svg class="abs" style="right:22px;top:173px" width="8" height="16" viewBox="0 0 8 16" aria-hidden="true"><path d="M1 1 C6 1 7 5 7 8 C7 11 6 15 1 15 L1 12 C3 12 4 10 4 8 C4 6 3 4 1 4 Z" fill="var(--white)"/></svg>
    <div class="abs" style="right:20px;top:254px;font-size:8px;color:var(--ink);white-space:nowrap">Open Mon-Fri | 9 AM - 9 PM</div>
    <div class="abs blue" style="right:20px;top:267px;font-size:8px;font-weight:600;white-space:nowrap">www.serenawellspa.com</div>
  </section>

</main>
</body>
</html>
```